Business Card Design

We are a business based in Sydney repairing and restoring timber windows. We mainly cater to residential home owners although sometimes work with larger building companies. We do a lot of work in heritage buildings though also cater to modern windows.
Our Logo is Black and Gold and were thinking of using a white card with only these two colours although we are open to any design suggestions. Check out our website for ideas.
Front of Card
Contact Information, Website & Business Name
Back of Card
Business Logo, website?
Target Market(s)
Home Owners
Industry/Entity Type
Residential
Contact Information for Business Card
Oakridge Sash Revivals
Marcus Pellow
0472 309 648
marcus@oakridgesashrevivals.example
www.oakridgesashrevivals.example
Look and feel

```html
<!DOCTYPE html>
<html lang="en">
<head>
<meta charset="utf-8">
<title>Marcus Pellow – Oakridge Sash Revivals</title>
<link rel="stylesheet" href="https://fonts.googleapis.com/css2?family=Source+Sans+3:wght@400;600;700&display=swap">
<style>
  :root {
    --card-white: #ffffff;
    --ink: #111111;
    --gold: #ffc229;
    --gold-mid: #ffd36a;
    --gold-pale: #fff1cc;
  }
  html, body {
    margin: 0;
    padding: 0;
    width: 1200px;
    height: 741px;
    overflow: hidden;
    background: var(--card-white);
  }
  .card {
    position: relative;
    width: 1200px;
    height: 741px;
    background: var(--card-white);
    font-family: "Source Sans 3", "Myriad Pro", Arial, sans-serif;
    color: var(--ink);
    overflow: hidden;
  }
  .brush-art {
    position: absolute;
    left: 0;
    top: 0;
    width: 720px;
    height: 741px;
  }
  .holder-name {
    position: absolute;
    right: 62px;
    top: 76px;
    margin: 0;
    font-size: 43px;
    font-weight: 700;
    letter-spacing: 0.2px;
    line-height: 1;
  }
  .contact-list {
    position: absolute;
    right: 62px;
    top: 512px;
    margin: 0;
    padding: 0;
    list-style: none;
  }
  .contact-item {
    display: flex;
    justify-content: flex-end;
    align-items: center;
    height: 54px;
    font-size: 25px;
    font-weight: 400;
  }
  .contact-item--phone { font-size: 28px; }
  .contact-icon {
    flex: none;
    margin-right: 30px;
    fill: var(--gold);
  }
  .contact-item--phone .contact-icon { margin-right: 20px; }
</style>
</head>
<body>
  <main class="card">
    <svg class="brush-art" viewBox="0 0 720 741" role="img" aria-label="Abstract gold brush-stroke artwork sweeping across the left side of the card">
      <defs>
        <radialGradient id="brushGlow" cx="0.3" cy="0.5" r="0.7">
          <stop offset="0" stop-color="var(--gold)" stop-opacity="0.95"/>
          <stop offset="0.55" stop-color="#ffc229" stop-opacity="0.75"/>
          <stop offset="0.85" stop-color="#ffd36a" stop-opacity="0.35"/>
          <stop offset="1" stop-color="#fff1cc" stop-opacity="0"/>
        </radialGradient>
      </defs>
      <path d="M0 0 H420 C410 120 440 220 400 300 C470 360 620 380 700 380 C600 450 520 560 500 741 H0 Z" fill="url(#brushGlow)"/>
    </svg>

    <h1 class="holder-name">Marcus Pellow</h1>

    <ul class="contact-list">
      <li class="contact-item contact-item--phone">
        <svg class="contact-icon" width="30" height="30" viewBox="0 0 24 24" aria-hidden="true">
          <path d="M6.6 10.8a15.1 15.1 0 0 0 6.6 6.6l2.2-2.2a1 1 0 0 1 1-.25 11.4 11.4 0 0 0 3.6.57 1 1 0 0 1 1 1V20a1 1 0 0 1-1 1A17 17 0 0 1 3 4a1 1 0 0 1 1-1h3.5a1 1 0 0 1 1 1c0 1.25.2 2.45.57 3.57a1 1 0 0 1-.25 1z"/>
        </svg>
        <span>0472 309 648</span>
      </li>
      <li class="contact-item contact-item--web">
        <svg class="contact-icon" width="36" height="36" viewBox="0 0 24 24" aria-hidden="true">
          <circle cx="12" cy="12" r="10" fill="none" stroke="var(--gold)" stroke-width="2"/>
          <path d="M7 7c2 0 3 1 3 2.5S8.5 12 9 13.5 11 15 11 17.5 10 20 10 20C6.5 19 4 16 4 12c0-2 1-3.8 3-5zM14 5c2 .5 4 2 4.8 4-1.3.3-2.3 0-3-.8S14 6.5 14 5zM15 13c1.5-.5 3.5 0 4.5 1-.8 2.5-2.5 4-4.5 4.8-.6-2 .5-3-.5-4.3z"/>
        </svg>
        <span>www.oakridgesashrevivals.example</span>
      </li>
      <li class="contact-item contact-item--email">
        <svg class="contact-icon" width="40" height="28" viewBox="0 0 40 28" aria-hidden="true">
          <rect x="0" y="0" width="40" height="28" rx="2"/>
          <path d="M1 1 L20 16 L39 1" fill="none" stroke="var(--card-white)" stroke-width="2.5"/>
        </svg>
        <span>marcus@oakridgesashrevivals.example</span>
      </li>
    </ul>
  </main>
</body>
</html>
```